依頼詳細
既存サイトのデザインが古くなったため、リニューアルを行います。
ワイヤーフレーム有。
参考サイト有。
https://www.morisuzu-web.jp/
今風でシンプルなデザインをお願いいたします。
メインカラーは緑で、現在のロゴをお渡ししますので、トレースしSVGで作ってください。
サイトURL
ページ数
1ページ
希望イメージ
シンプル 複雑
単色 カラフル
暗い 明るい
日常 高級
遊び心 厳粛
未来的 伝統的
女性的 男性的
希望する色
緑系
納品ファイル
• イラストレーター形式 (.ai)
補足説明
TOPページ(PC版とスマホ版)のみご提案ください。
採用した場合は、アーカイブと詳細ページ(スタイルガイド)のデザインもお願いいたします。
ワイヤーフレームではなく、サイトマップ有です。
締め切りを10日後に変更しました。
URLの記載があるのは、参考サイトです。
会社名はダミー(株式会社ダミーリサイクル)とし、
添付のサイトマップに合わせて作っていただけると幸いです。
記載内容がややこしくて申し訳ございません。
その他文言等もダミーで結構です。
よろしくお願いいたします。
■ 選んだ理由

シンプルかつ、今風なレイアウトで好感が持てました。

■ 提案者全員のお礼・コメント

修正依頼にも迅速に対応いただき、ありがとうございました。
またご提案よろしくお願いいたします。

```html
<!DOCTYPE html>
<html lang="ja">
<head>
<meta charset="utf-8">
<title>株式会社ダミーリサイクル</title>
<link rel="stylesheet" href="https://fonts.googleapis.com/css2?family=Noto+Sans+JP:wght@400;500;700&family=Oswald:wght@500;600&display=swap">
<style>
:root{
  --green:#2f8f6e;
  --green-light:#3ba483;
  --green-dark:#217a5c;
  --ink:#222;
  --muted:#666;
  --line:#dcdcdc;
  --bg-gray:#f5f5f5;
  --bg-blue:#ebf2f8;
  --white:#fff;
}
*{box-sizing:border-box;margin:0;padding:0}
html,body{width:1200px;height:4104px;overflow:hidden}
body{position:relative;font-family:"Noto Sans JP",sans-serif;color:var(--ink);background:var(--white)}
.abs{position:absolute}
.en{font-family:"Oswald",sans-serif;font-weight:600;letter-spacing:.02em}
.btn{position:absolute;display:flex;align-items:center;justify-content:center;background:var(--green);color:#fff;font-size:13px;letter-spacing:.1em}
.sec-title{position:absolute;left:0;width:1200px;text-align:center}
.sec-title .en{display:block;font-size:32px;color:var(--ink)}
.sec-title .ja{display:block;font-size:12px;color:var(--muted);margin-top:6px}
.photo{position:absolute}
.body-text{font-size:13px;line-height:2.1;color:#444;letter-spacing:.08em}

/* header */
.site-header{top:0;left:0;width:1200px;height:72px;background:#fff}
.brand{left:24px;top:26px;font-size:15px;font-weight:700}
.gnav{right:160px;top:27px;display:flex;gap:26px;font-size:13px}
.header-contact{right:0;top:0;width:120px;height:80px;flex-direction:column;font-size:12px;gap:6px}

/* hero */
.hero{top:72px;left:0;width:1200px;height:600px;background:linear-gradient(180deg,#2c8fd6 0%,#6cbbe9 45%,#c7e2f3 58%,#7fb9e0 75%,#a9d3ef 100%)}
.hero-title{left:160px;top:290px;color:#fff;font-size:40px;font-weight:500;letter-spacing:.12em}
.hero-sub{left:160px;top:360px;color:#fff;font-size:13px;letter-spacing:.15em}
.hero-scroll{left:599px;top:610px;width:1px;height:62px;background:#fff}

/* business */
.business{top:672px;left:0;width:1200px;height:580px;background:var(--bg-gray)}
.biz-card{top:876px;width:280px;height:212px;display:flex;align-items:center;justify-content:center;color:#fff;font-size:20px;font-weight:700;letter-spacing:.1em}

/* product */
.product-bg{top:1252px;left:0;width:1200px;height:530px;background:var(--bg-gray)}
.product-box{top:1330px;left:0;width:560px;height:452px;background:#fff}

/* column */
.column{top:1760px;left:0;width:1200px;height:660px;background:var(--bg-blue)}
.col-card{top:1988px;width:280px;height:272px;background:#fff}
.col-card .img{height:176px}
.col-card .date{font-size:11px;color:var(--muted);padding:16px 20px 4px}
.col-card .ttl{font-size:13px;font-weight:500;padding:0 20px}

/* news */
.news-row{left:160px;width:880px;height:60px;border-bottom:1px solid var(--line);display:flex;align-items:center;font-size:13px}
.news-row .date{width:120px;color:var(--muted);font-size:12px}

/* contact */
.contact{top:3440px;left:0;width:1200px;height:460px;background:linear-gradient(120deg,var(--green-dark) 0%,var(--green) 50%,var(--green-light) 100%)}
.contact-frame{top:3600px;left:160px;width:880px;height:180px;border:1px solid rgba(255,255,255,.7)}

/* footer */
.footer-nav{font-size:12px;display:flex;gap:28px}
</style>
</head>
<body>

<header class="abs site-header">
  <div class="abs brand">株式会社ダミーリサイクル</div>
  <nav class="abs gnav"><span>会社情報</span><span>事業紹介</span><span>商品情報</span><span>コラム</span><span>環境報告書</span><span>採用情報</span></nav>
  <a class="btn header-contact"><svg width="20" height="14" viewBox="0 0 20 14"><rect x="1" y="1" width="18" height="12" fill="none" stroke="#fff" stroke-width="1.5"/><path d="M1 1l9 7 9-7" fill="none" stroke="#fff" stroke-width="1.5"/></svg>お問い合わせ</a>
</header>

<section class="abs hero" role="img" aria-label="海辺に広がる高層ビル街と水面に映る街並みの写真"></section>
<h1 class="abs hero-title">ダミーテキスト</h1>
<p class="abs hero-sub">ダミーテキスト ダミーテキスト ダミーテキスト ダミーテキスト</p>
<div class="abs hero-scroll"></div>

<section class="abs business"></section>
<div class="sec-title" style="top:764px"><span class="en">BUSINESS</span><span class="ja">事業紹介</span></div>
<div class="abs biz-card" style="left:160px;background:linear-gradient(135deg,#5e9a3a,#9cc664)" role="img" aria-label="緑の葉の写真">環境事業</div>
<div class="abs biz-card" style="left:460px;background:linear-gradient(135deg,#1f2f52,#4f6f9e)" role="img" aria-label="夜の道路を走る車の光跡の写真">運搬事業</div>
<div class="abs biz-card" style="left:760px;background:linear-gradient(135deg,#5f84ad,#c3d6e9)" role="img" aria-label="見上げた高層ビルの写真">建設事業</div>
<a class="btn" style="left:500px;top:1132px;width:200px;height:40px">事業紹介</a>

<section class="abs product-bg"></section>
<div class="abs product-box"></div>
<div class="photo" style="left:500px;top:1262px;width:700px;height:460px;background:linear-gradient(135deg,#8a8a86,#c9c8c2 50%,#9a9993)" role="img" aria-label="積み上げられた砕石の写真"></div>
<div class="abs" style="left:160px;top:1412px"><span class="en" style="display:block;font-size:32px">PRODUCT</span><span style="font-size:12px;color:var(--muted)">商品情報</span></div>
<p class="abs body-text" style="left:160px;top:1512px;width:310px">ダミーテキストダミーテキストダミーテキストダミーテキストダミーテキストダミーテキストダミーテキストダミーテキストダミーテキストダミーテキストダミーテキスト</p>
<a class="btn" style="left:160px;top:1668px;width:200px;height:40px">商品情報</a>

<section class="abs column"></section>
<div class="abs" style="top:1720px;left:0;width:1040px;height:60px;background:var(--bg-gray)"></div>
<div class="sec-title" style="top:1880px"><span class="en">COLUMN</span><span class="ja">コラム</span></div>
<article class="abs col-card" style="left:160px"><div class="img" style="background:linear-gradient(180deg,#b9d3e8,#d8c9a8)" role="img" aria-label="砂利の山とベルトコンベアの写真"></div><p class="date">2023.01.10</p><p class="ttl">コラムのタイトルが入ります</p></article>
<article class="abs col-card" style="left:460px"><div class="img" style="background:linear-gradient(180deg,#9fc7e4,#8fb87a)" role="img" aria-label="緑に囲まれたオフィス街の写真"></div><p class="date">2023.01.10</p><p class="ttl">コラムのタイトルが入ります</p></article>
<article class="abs col-card" style="left:760px"><div class="img" style="background:linear-gradient(180deg,#c9b79d,#8c8f96)" role="img" aria-label="倉庫に荷物が積まれたトラックの写真"></div><p class="date">2023.01.10</p><p class="ttl">コラムのタイトルが入ります</p></article>
<a class="btn" style="left:500px;top:2292px;width:200px;height:40px">一覧</a>

<div class="sec-title" style="top:2512px"><span class="en">NEWS</span><span class="ja">お知らせ</span></div>
<div class="abs news-row" style="top:2620px;border-top:1px solid var(--line)"><span class="date">2023.01.10</span>お知らせのタイトルが入ります</div>
<div class="abs news-row" style="top:2680px"><span class="date">2023.01.10</span>お知らせのタイトルが入ります</div>
<div class="abs news-row" style="top:2740px"><span class="date">2023.01.10</span>お知らせのタイトルが入ります</div>
<a class="btn" style="left:500px;top:2848px;width:200px;height:40px">一覧</a>

<div class="photo" style="left:0;top:2980px;width:700px;height:452px;background:linear-gradient(135deg,#c24a3a 0%,#d9d6d0 30%,#9fa3a8 70%,#6f7479)" role="img" aria-label="建設現場で作業員二人が資料を確認している写真"></div>
<div class="abs" style="left:740px;top:3116px"><span class="en" style="display:block;font-size:32px">RECRUIT</span><span style="font-size:12px;color:var(--muted)">採用情報</span></div>
<p class="abs body-text" style="left:740px;top:3200px;width:310px">ダミーテキストダミーテキストダミーテキストダミーテキストダミーテキストダミーテキストダミーテキストダミーテキストダミーテキストダミーテキストダミーテキスト</p>
<a class="btn" style="left:740px;top:3392px;width:208px;height:40px">採用情報</a>

<section class="abs contact"></section>
<div class="abs contact-frame"></div>
<div class="abs" style="left:160px;top:3640px;width:440px;text-align:center;color:#fff"><span class="en" style="display:block;font-size:30px">CONTACT</span><span style="font-size:12px">お問い合わせ</span><p style="font-size:12px;margin-top:22px;line-height:1.9">ご相談・ご質問等ございましたら<br>お気軽にお問い合わせください</p></div>
<div class="abs" style="left:600px;top:3630px;width:1px;height:120px;background:rgba(255,255,255,.7)"></div>
<div class="abs" style="left:600px;top:3634px;width:440px;text-align:center;color:#fff">
  <div style="display:flex;align-items:center;justify-content:center;gap:10px;font-size:34px;font-weight:500"><svg width="26" height="26" viewBox="0 0 24 24"><path fill="#fff" d="M6.6 10.8c1.4 2.8 3.8 5.1 6.6 6.6l2.2-2.2c.3-.3.7-.4 1-.2 1.1.4 2.3.6 3.6.6.6 0 1 .4 1 1V20c0 .6-.4 1-1 1C10.6 21 3 13.4 3 4c0-.6.4-1 1-1h3.5c.6 0 1 .4 1 1 0 1.3.2 2.5.6 3.6.1.3 0 .7-.2 1z"/></svg>000-000-0000</div>
  <p style="font-size:11px;margin-top:4px">受付時間 平日 9:00～18:00</p>
  <a class="btn" style="position:relative;margin:16px auto 0;width:200px;height:38px;background:#fff;color:var(--green)">お問い合わせ</a>
</div>

<footer>
  <div class="abs" style="left:160px;top:3932px;font-size:15px;font-weight:700">株式会社ダミーリサイクル</div>
  <p class="abs" style="left:160px;top:3976px;font-size:11px;line-height:1.8;color:#444">〒000-0000 東京都○○区○○ 0-0-0<br>TEL 000-000-0000　FAX 000-000-0000</p>
  <nav class="abs footer-nav" style="left:640px;top:3936px"><span>会社情報</span><span>事業紹介</span><span>商品情報</span><span>コラム</span><span>環境報告書</span><span>採用情報</span></nav>
  <nav class="abs footer-nav" style="left:640px;top:3980px"><span>お知らせ</span><span>お問い合わせ</span><span>プライバシーポリシー</span><span>サイトマップ</span></nav>
  <p class="abs" style="right:160px;top:4056px;font-size:10px;color:var(--muted)">© DUMMY RECYCLE ALL RIGHTS RESERVED.</p>
</footer>

</body>
</html>
```